BQN Project Signage

Need a sign to be displayed in the front of properties currently under Construction or Renovation to advertise our company information. Need it to be Professional and Contemporary. We are a Design/Build Construction Company. Information should include Company Name, email, website, phone number. Attached: Logo and company brochure, also included and inspiration images

```html
<!DOCTYPE html>
<html lang="en">
<head>
<meta charset="utf-8">
<title>BQN Project Signage</title>
<link href="https://fonts.googleapis.com/css2?family=Montserrat:wght@400;500;700;800&display=swap" rel="stylesheet">
<style>
  :root {
    --page-bg: #ffffff;
    --sign-light: #ececec;
    --ink: #0b0b0b;
    --accent: #f0ee45;
    --white: #ffffff;
    --photo-warm: #d9cbb5;
    --photo-deep: #7a6a55;
  }
  html, body {
    margin: 0;
    padding: 0;
    width: 1200px;
    height: 1200px;
    overflow: hidden;
    background: var(--page-bg);
    font-family: "Montserrat", sans-serif;
  }
  .sign {
    position: absolute;
    left: 233px;
    top: 54px;
    width: 734px;
    height: 1097px;
    background: var(--sign-light);
    overflow: hidden;
    box-shadow: 0 6px 18px rgba(0,0,0,0.25);
  }
  .top-rule {
    position: absolute;
    left: 0;
    top: 22px;
    width: 365px;
    height: 15px;
    background: var(--ink);
  }
  .brand {
    position: absolute;
    left: 236px;
    top: 120px;
    display: flex;
    align-items: center;
    gap: 14px;
    white-space: nowrap;
    color: var(--ink);
    font-weight: 500;
    font-size: 34px;
    line-height: 1;
    letter-spacing: 1px;
  }
  .brand-dot {
    width: 22px;
    height: 22px;
    border-radius: 50%;
    background: var(--accent);
    flex: none;
  }
  .dot-grid {
    position: absolute;
    left: 23px;
    top: 186px;
  }
  .lower-panel {
    position: absolute;
    left: 0;
    top: 508px;
    width: 734px;
    height: 430px;
    background:
      repeating-linear-gradient(135deg, rgba(255,255,255,0) 0 60px, rgba(255,255,255,0.05) 60px 64px, rgba(255,255,255,0) 64px 130px),
      var(--ink);
  }
  .photo {
    position: absolute;
    left: 69px;
    top: 326px;
    width: 592px;
    height: 362px;
    border: 3px solid var(--ink);
    background: linear-gradient(160deg, var(--photo-warm) 0%, #efe6d8 45%, var(--photo-deep) 100%);
  }
  .headline {
    position: absolute;
    left: 0;
    top: 728px;
    width: 734px;
    text-align: center;
    white-space: nowrap;
    color: var(--white);
    font-weight: 800;
    font-size: 72px;
    line-height: 1;
    letter-spacing: -0.5px;
  }
  .contact {
    position: absolute;
    left: 60px;
    display: flex;
    align-items: center;
    gap: 22px;
    white-space: nowrap;
    color: var(--white);
    font-weight: 500;
    font-size: 35px;
    line-height: 1;
  }
  .contact svg { width: 34px; height: 34px; flex: none; }
  .contact-email { top: 818px; }
  .contact-web { top: 877px; }
  .phone-band {
    position: absolute;
    left: 0;
    top: 938px;
    width: 734px;
    height: 159px;
    background: var(--accent);
    color: var(--ink);
    text-align: center;
  }
  .phone-line {
    position: absolute;
    left: 0;
    width: 100%;
    font-size: 44px;
    line-height: 1;
    font-weight: 400;
  }
  .phone-line strong { font-weight: 800; }
  .phone-direct { top: 17px; }
  .phone-office { top: 101px; }
  .phone-divider {
    position: absolute;
    left: 93px;
    top: 79px;
    width: 547px;
    height: 5px;
    background: var(--ink);
  }
</style>
</head>
<body>
  <div class="sign">
    <div class="top-rule"></div>

    <div class="brand"><span class="brand-dot"></span>BQN CONSTRUCTION</div>

    <svg class="dot-grid" width="110" height="130" viewBox="0 0 110 130" aria-hidden="true">
      <defs>
        <pattern id="dots" width="24" height="24" patternUnits="userSpaceOnUse">
          <circle cx="3" cy="3" r="2.4" fill="#0b0b0b"/>
        </pattern>
      </defs>
      <rect x="0" y="0" width="106" height="126" fill="url(#dots)"/>
    </svg>

    <div class="lower-panel"></div>

    <div class="photo" role="img" aria-label="Photo of a luxury living room with white tufted sofa, brass chandelier and marble feature wall"></div>

    <div class="headline">BQN Construction</div>

    <div class="contact contact-email">
      <svg viewBox="0 0 34 34" aria-hidden="true">
        <rect x="3" y="8" width="28" height="20" fill="none" stroke="#f0ee45" stroke-width="2.2"/>
        <path d="M3 8 L17 20 L31 8 M3 28 L13 17 M31 28 L21 17" fill="none" stroke="#f0ee45" stroke-width="2.2"/>
      </svg>
      <span>marc@bqnconstruction.com</span>
    </div>

    <div class="contact contact-web">
      <svg viewBox="0 0 34 34" aria-hidden="true">
        <circle cx="17" cy="17" r="14" fill="#f0ee45"/>
        <g fill="none" stroke="#0b0b0b" stroke-width="1.6">
          <ellipse cx="17" cy="17" rx="6" ry="14"/>
          <line x1="17" y1="3" x2="17" y2="31"/>
          <line x1="3" y1="17" x2="31" y2="17"/>
          <line x1="5" y1="10" x2="29" y2="10"/>
          <line x1="5" y1="24" x2="29" y2="24"/>
        </g>
      </svg>
      <span>www.bqnconstruction.com</span>
    </div>

    <div class="phone-band">
      <div class="phone-line phone-direct">Direct: <strong>561.555.0148</strong></div>
      <div class="phone-divider"></div>
      <div class="phone-line phone-office">Office: <strong>561.555.0172</strong></div>
    </div>
  </div>
</body>
</html>
```